Quorvanta Brochure Design

Want a brochure done for quorvanta company. [www.quorvanta-example.com]
We are a software development/Staffing/IT services company based in US, UK and India.
I want a brochure done to reflect "techie" theme. The brochure must be a 2 fold 8.5 * 11 design with an inside sleeve. The inside sleeve will carry pages from www.quorvanta-example.com
Of course you are free to borrow content from www.quorvanta-example.com. however, I value "original" designs.

Target Market(s)

All industry verticals [ex: banking, insurance, medical etc] that have IT operations/staffing needs.

Industry/Entity Type

Software

Colors
f68d4d
faf289
85abd2

Requirements
Must have
• Professional/eye catching design

```html
<!DOCTYPE html>
<html lang="en">
<head>
<meta charset="utf-8">
<title>Quorvanta Brochure – Inside Spread</title>
<link rel="stylesheet" href="https://fonts.googleapis.com/css2?family=Montserrat:wght@500;600&family=Ubuntu:wght@400;500;700&display=swap">
<style>
  :root {
    --backdrop: #b9b9b9;
    --paper: #ffffff;
    --paper-shade: #f3f3f3;
    --band-grey: #8a8a8c;
    --band-grey-dark: #6f7073;
    --accent-orange: #f0892a;
    --heading-blue: #1f8fd3;
    --body-text: #4a4a4a;
    --photo-light: #dbe8f2;
    --photo-mid: #9fbfd9;
    --photo-deep: #5f86a8;
  }
  * { box-sizing: border-box; margin: 0; padding: 0; }
  html, body { width: 1200px; height: 847px; overflow: hidden; }
  body {
    background: var(--backdrop);
    font-family: "Ubuntu", Arial, sans-serif;
    color: var(--body-text);
  }
  .spread {
    position: absolute;
    left: 60px; top: 48px;
    width: 1080px; height: 750px;
    display: flex;
    box-shadow: 0 12px 30px rgba(0,0,0,.25);
  }
  .page {
    position: relative;
    width: 540px; height: 750px;
    background: var(--paper);
    overflow: hidden;
  }
  .page--left { background: linear-gradient(90deg, var(--paper) 85%, var(--paper-shade)); }
  .page--right { background: linear-gradient(90deg, var(--paper-shade), var(--paper) 12%); }

  .hero-photo {
    position: absolute; left: 0; top: 0;
    width: 540px; height: 290px;
    background: linear-gradient(120deg, var(--photo-light) 0%, var(--photo-mid) 45%, var(--photo-deep) 100%);
  }
  .section-band {
    position: absolute;
    color: #fff;
    font-family: "Montserrat", Arial, sans-serif;
    font-weight: 500;
    letter-spacing: 1px;
  }
  .section-band--about {
    left: 0; top: 244px; width: 540px; height: 56px;
    background: linear-gradient(90deg, var(--band-grey-dark) 0%, var(--band-grey-dark) 45%, rgba(111,112,115,.55) 100%);
    font-size: 22px; padding: 14px 0 0 44px;
  }
  .section-band--services {
    left: 0; top: 0; width: 540px; height: 56px;
    background: var(--band-grey);
    font-size: 22px; padding: 16px 0 0 28px;
  }
  .about-copy {
    position: absolute; left: 44px; top: 318px; width: 470px;
    font-size: 11px; line-height: 1.4;
  }
  .about-copy p { margin-bottom: 9px; }
  .page-footer {
    position: absolute; left: 0; bottom: 0; width: 540px; height: 42px;
    background: var(--accent-orange);
    color: #fff; font-size: 12px; padding-top: 14px;
  }
  .page--left .page-footer { padding-left: 44px; }
  .page--right .page-footer { text-align: right; padding-right: 30px; }
  .page-footer strong { font-weight: 700; }

  .services { position: absolute; left: 28px; top: 76px; width: 484px; }
  .service { margin-bottom: 16px; }
  .service-title {
    color: var(--heading-blue);
    font-family: "Ubuntu", Arial, sans-serif;
    font-weight: 700; font-size: 17px;
    margin-bottom: 6px;
  }
  .service-copy { font-size: 11px; line-height: 1.45; }
  .service-tagline {
    display: flex; align-items: center; gap: 8px;
    font-size: 12.5px; color: #222; margin: 4px 0 8px;
  }
  .service-tagline svg { flex: none; }
</style>
</head>
<body>
<main class="spread">
  <section class="page page--left">
    <div class="hero-photo" role="img" aria-label="Photo of a smiling businesswoman touching a holographic interface with a world map and charts"></div>
    <h2 class="section-band section-band--about">ABOUT US</h2>
    <div class="about-copy">
      <p>We develop IT solutions for Top 500 corporations, small-medium corporations, global outsourcers and government agencies and live by our creed</p>
      <p>To create value while always exceeding expectations with our customer by offering Information Technology consulting, outsourcing and staffing solutions through commitment, innovation and service excellence.</p>
      <p>At Quorvanta our success comes through "partnering" with our customers.</p>
      <p>From our ongoing commitment to delivering the highest quality products and services, to the way we engage with our customers, we make sure everything we do is centralized around our core "partnership" approach – Your success depends on our ability to understand your business vision, and to build a high performance team focused on innovation, excellence and integrity. Every employee makes this personal commitment to your success and it's this type of passion of our employees that differentiates Quorvanta.</p>
      <p>Headquartered in Brookvale, NC in USA since 2012, Quorvanta understands our client business needs and uses technology to translate the challenges into improvements. Our knowledge, experience, scope, expertise allows us to offer distinctive, quality, cost effective and lasting solutions by improving time to market to our clients to do their business better.</p>
      <p>Core Values • Our people are our strength and we are committed to our employees • We fulfill our commitments and act with integrity • We embrace change and reward innovation • We have only one standard – "excellence" Address: 418 Larchmont Ridge Dr, Brookvale NC 27000</p>
    </div>
    <footer class="page-footer">www.<strong>quorvanta</strong>-example.com</footer>
  </section>

  <section class="page page--right">
    <h2 class="section-band section-band--services">SERVICES</h2>
    <div class="services">
      <article class="service">
        <h3 class="service-title">Software Consulting/Staffing</h3>
        <p class="service-copy">In the fast changing world of technology, Quorvanta's consultants have industry leading experience in .Nexa, JX2, SRP, Big Data, Orvex, QA and many other technologies. Get your return on investment quicker with Quorvanta's dedicated and goal oriented consultants that can deliver results on time and budget.</p>
      </article>
      <article class="service">
        <h3 class="service-title">.Nexa/JX2/SRP/Big Data/QA</h3>
        <div class="service-tagline">
          <svg width="26" height="26" viewBox="0 0 26 26" aria-hidden="true"><rect x="2" y="6" width="18" height="18" fill="none" stroke="var(--heading-blue)" stroke-width="2.5"/><path d="M10 17 L22 3 L25 6 L13 20 L9 21 Z" fill="var(--heading-blue)"/></svg>
          Quality Consulatants
        </div>
        <p class="service-copy">Our consultants have vast in the above technologies and can get your project up and running in very quick time. We have consultants experienced in end to end SDLC using latest programing techniques. We train our consultants on techniques like TTD (Test driven development), Design Patterns etc. so that our clients can have a world class software solution.</p>
      </article>
      <article class="service">
        <h3 class="service-title">Custom Sofware Development</h3>
        <div class="service-tagline">
          <svg width="26" height="26" viewBox="0 0 26 26" aria-hidden="true"><circle cx="13" cy="13" r="10.5" fill="none" stroke="var(--heading-blue)" stroke-width="3"/><path d="M13 7 V13 H18" fill="none" stroke="var(--heading-blue)" stroke-width="2.5"/></svg>
          Software powers the world!
        </div>
        <p class="service-copy">Software is complex. Especially with systems spanning multiple platforms and web/system service layers. We have a in-house software development shop that takes care of creating/managing complex software systems. We provide the client weekly updates on the project status. We follow SCRUM software methodology. We have expertise in using TDX, Trakka/Revstore for ALM/Source control versioning.</p>
      </article>
      <article class="service">
        <h3 class="service-title">Back Office Processing</h3>
        <div class="service-tagline">
          <svg width="24" height="28" viewBox="0 0 24 28" aria-hidden="true"><path d="M6 12 V8 A6 6 0 0 1 18 8" fill="none" stroke="var(--heading-blue)" stroke-width="3"/><rect x="2" y="12" width="20" height="15" rx="2" fill="var(--heading-blue)"/><circle cx="12" cy="19" r="2" fill="#fff"/></svg>
          It is not a black box!
        </div>
        <p class="service-copy">Sometimes Back office processing is over whelming to our clients. With no clear visibility on what's happening to data/systems, it can get hard to get the right information. We partnered with some reputed BPO providers in India to give you full spectrum visibility to your back office projects.</p>
      </article>
    </div>
    <footer class="page-footer">www.<strong>quorvanta</strong>-example.com</footer>
  </section>
</main>
</body>
</html>
```